Website Design - Photo Shop Design - Functional Cash Register Layout for POS System

Design a webpage for Point of Sale site. A cash register page.

Page must have a good look. I have attached a file of a possible layout example - but need a much nicer design. I have also attached the site logo. which i will upload without background tomorrow hopefully.

Looking for a nice Fresh look , not dark and dingy.

Target Market(s)

Business

Industry/Entity Type

Business Software

Number of Pages Required

1 page

Colors
f59195
f04a50
ec1f27
fbd4d5
ffffff
f8f3f8
fdf0f6
feeeee
ecf5f6

Requirements
Must have
• Cash register layout for POS software site. Nice layout ,
Nice to have
• Try putting he register part on the left side as well as the right - invert the designs have them different to the layout example shown too.
Should not have
• Not to dark

```html
<!DOCTYPE html>
<html lang="en">
<head>
<meta charset="utf-8">
<title>TillNest – Cash Register</title>
<link rel="stylesheet" href="https://fonts.googleapis.com/css2?family=Roboto:wght@300;400;500&display=swap">
<style>
:root{
  --red:#f04a50;
  --red-deep:#ec1f27;
  --rose:#f59195;
  --blush:#fbd4d5;
  --header:#fcdcdd;
  --page:#fdf0f6;
  --tile:#f4eeee;
  --tile-text:#b9a9a9;
  --row:#f2ecec;
  --line:#ececec;
  --white:#ffffff;
  --text:#333333;
  --muted:#8a8a8a;
}
*{box-sizing:border-box;margin:0;padding:0}
html,body{width:1200px;height:751px;overflow:hidden}
body{font-family:"Roboto",Arial,sans-serif;color:var(--text);background:var(--page);position:relative;font-size:12px}
.abs{position:absolute}

/* top bar */
.topbar{left:0;top:0;width:1200px;height:64px;background:var(--header)}
.brand{left:0;top:0;width:180px;height:64px;background:var(--white);display:flex;align-items:center;padding-left:16px;gap:8px}
.brand-dot{width:18px;height:18px;border-radius:50%;background:var(--red)}
.brand-name{font-size:21px;font-weight:500;color:var(--red)}
.register-btn{left:203px;top:17px;width:186px;height:30px;background:var(--rose);color:var(--white);font-size:12.5px;display:flex;align-items:center;padding-left:11px;gap:14px}
.badge{width:17px;height:17px;border-radius:50%;background:var(--white);color:var(--rose);font-size:10px;display:flex;align-items:center;justify-content:center}
.search{left:409px;top:17px;width:207px;height:30px;background:var(--white);display:flex;align-items:center;padding-left:10px;gap:8px;color:#aaa;font-size:12px}
.icon-btn{top:22px}
.menu-btn{left:1154px;top:24px}

/* sidebar */
.sidebar{left:0;top:64px;width:180px;height:687px;background:var(--white);border-right:1px solid var(--line)}
.avatar{left:13px;top:89px;width:51px;height:51px;border-radius:50%;background:linear-gradient(135deg,#e8d6c8,#b9a394)}
.greet{left:75px;top:97px;font-size:13px;line-height:17px}
.greet .role{color:var(--red);font-weight:500}
.nav{left:0;top:158px;width:180px;list-style:none}
.nav li{height:40px;display:flex;align-items:center;padding:0 10px;gap:11px;border-bottom:1px solid var(--line);font-size:12.5px}
.nav li.active{background:var(--rose);color:var(--white);height:34px;margin-bottom:4px;border-bottom:none}
.nav-icon{width:19px;height:19px;background:var(--red);border-radius:2px;flex:none;display:flex;align-items:center;justify-content:center}
.nav li.active .nav-icon{background:var(--red)}
.nav .count{margin-left:auto;width:17px;height:17px;border-radius:50%;background:var(--red);color:var(--white);font-size:10px;display:flex;align-items:center;justify-content:center}
.store-badge{left:16px;top:693px;width:120px;height:38px;border-radius:5px;background:#e9e4e4}

/* panels */
.panel{background:var(--white)}
.panel-head{height:38px;border-bottom:1px solid var(--blush);display:flex;align-items:center;padding-left:16px;gap:9px;font-size:14px}
.head-dot{width:15px;height:15px;border-radius:50%;background:var(--red)}

.products{left:203px;top:89px;width:664px;height:362px}
.tile{width:112px;height:103px;background:var(--tile);text-align:center}
.tile b{display:block;font-weight:300;font-size:42px;color:var(--tile-text);padding-top:16px;height:82px}
.tile span{display:block;height:21px;line-height:21px;background:var(--rose);color:var(--white);font-size:12px;white-space:nowrap;overflow:hidden;text-overflow:ellipsis;padding:0 4px}
.pager{top:316px;width:77px;height:31px;background:var(--tile);color:var(--muted);font-size:12px;display:flex;align-items:center;justify-content:center}

.sales{left:203px;top:477px;width:664px;height:250px}
.legend{right:16px;top:11px;display:flex;gap:18px;font-size:12.5px}
.legend i{display:inline-block;width:13px;height:13px;vertical-align:-2px;margin-right:6px}
.legend .a{color:var(--red)} .legend .a i{background:var(--red)}
.legend .b{color:var(--rose)} .legend .b i{background:var(--blush)}
.chart{left:0;top:36px}
.tip{left:70px;top:59px;width:123px;height:82px;background:var(--red);color:var(--white);text-align:center}
.tip b{display:block;font-weight:300;font-size:42px;line-height:46px;padding-top:4px}
.tip span{display:block;font-size:12px;line-height:15px}

.customer{left:893px;top:89px;width:282px;height:587px}
.customer .panel-head{border-bottom:none;justify-content:flex-start}
.chev{margin-left:auto;margin-right:14px}
.txn{left:0;top:38px;width:282px;height:30px;background:var(--row);font-size:12px;display:flex;align-items:center;padding-left:14px}
.txn em{font-style:normal;color:var(--red);margin-left:4px}
.notes{left:14px;top:384px;color:var(--red);text-decoration:underline;font-size:12px}
.totals{left:0;top:407px;width:282px;list-style:none}
.totals li{height:24px;background:var(--row);border-bottom:1px solid var(--white);display:flex;align-items:center;justify-content:space-between;padding:0 20px 0 14px;font-size:12px}
.totals li span:last-child{color:var(--red)}
.btn{top:542px;width:116px;height:30px;font-size:12px;letter-spacing:.5px;display:flex;align-items:center;justify-content:center}
.btn-save{left:16px;background:#f6babc;color:var(--red);border:1px solid var(--rose)}
.btn-pay{left:150px;background:var(--red);color:var(--white)}

.chat{left:1133px;top:695px;width:40px;height:32px;background:var(--red);display:flex;align-items:center;justify-content:center}
</style>
</head>
<body>

<header class="abs topbar"></header>
<div class="abs brand"><span class="brand-dot"></span><span class="brand-name">TillNest</span></div>
<div class="abs register-btn">My Cash / Cash Register <span class="badge">2</span></div>
<div class="abs search">
  <svg width="12" height="12" viewBox="0 0 12 12"><circle cx="5" cy="5" r="3.8" fill="none" stroke="#f04a50" stroke-width="1.6"/><line x1="8" y1="8" x2="11" y2="11" stroke="#f04a50" stroke-width="1.6"/></svg>
  Search
</div>
<svg class="abs icon-btn" style="left:639px" width="18" height="18" viewBox="0 0 18 18"><circle cx="9" cy="9" r="5.5" fill="none" stroke="#f04a50" stroke-width="3" stroke-dasharray="2.6 1.7"/><circle cx="9" cy="9" r="3.6" fill="#f04a50"/><circle cx="9" cy="9" r="1.6" fill="#fcdcdd"/></svg>
<svg class="abs icon-btn" style="left:673px" width="18" height="18" viewBox="0 0 18 18"><circle cx="9" cy="9" r="7" fill="none" stroke="#f04a50" stroke-width="1.8"/><path d="M9 5v4.5h3" fill="none" stroke="#f04a50" stroke-width="1.8"/></svg>
<svg class="abs menu-btn" width="22" height="17" viewBox="0 0 22 17"><rect y="0" width="22" height="2.5" fill="#f04a50"/><rect y="7" width="22" height="2.5" fill="#f04a50"/><rect y="14" width="22" height="2.5" fill="#f04a50"/></svg>

<aside class="abs sidebar"></aside>
<div class="abs avatar" role="img" aria-label="User profile photo"></div>
<div class="abs greet">Hi, John Doe<br><span class="role">Admin</span></div>
<ul class="abs nav">
  <li class="active"><span class="nav-icon"><svg width="9" height="7"><rect x="0.5" y="0.5" width="8" height="5" fill="none" stroke="#fff"/></svg></span>Enter Sale</li>
  <li><span class="nav-icon"><svg width="9" height="9"><circle cx="4.5" cy="4" r="3" fill="#fff"/></svg></span>Parked/Layby Orders</li>
  <li><span class="nav-icon"><svg width="9" height="9"><path d="M1 3l3.5 3L8 3" fill="none" stroke="#fff" stroke-width="1.5"/></svg></span>Completed Sales<span class="count">3</span></li>
  <li><span class="nav-icon"><svg width="9" height="7"><rect x="0.5" y="0.5" width="8" height="5" fill="none" stroke="#fff"/></svg></span>Appointments<span class="count">5</span></li>
  <li><span class="nav-icon"><svg width="9" height="9"><circle cx="4" cy="4" r="2.6" fill="none" stroke="#fff" stroke-width="1.2"/><line x1="6" y1="6" x2="8.5" y2="8.5" stroke="#fff" stroke-width="1.2"/></svg></span>Back Office<span class="count">2</span></li>
  <li><span class="nav-icon"><svg width="9" height="9"><circle cx="4.5" cy="4.5" r="3.2" fill="none" stroke="#fff" stroke-width="1.2" stroke-dasharray="15 5"/></svg></span>Refresh Data</li>
</ul>
<div class="abs store-badge" role="img" aria-label="App store badge"></div>

<section class="abs panel products">
  <div class="panel-head"><span class="head-dot"></span>Products Stats</div>
  <div class="abs tile" style="left:17px;top:54px"><b>DP</b><span>Demo Product</span></div>
  <div class="abs tile" style="left:146px;top:54px"><b>EL</b><span>Entry Level Co...</span></div>
  <div class="abs tile" style="left:276px;top:54px"><b>GC</b><span>Gift Cards</span></div>
  <div class="abs tile" style="left:405px;top:54px"><b>P5</b><span>Product 5</span></div>
  <div class="abs tile" style="left:534px;top:54px"><b>T2</b><span>Test 2</span></div>
  <div class="abs tile" style="left:146px;top:172px"><b>T3</b><span>Test 3</span></div>
  <div class="abs tile" style="left:276px;top:172px"><b>FA</b><span>fasdfadfasdf</span></div>
  <div class="abs tile" style="left:405px;top:172px"><b>P3</b><span>Product 3</span></div>
  <div class="abs pager" style="left:17px">Previous</div>
  <div class="abs pager" style="left:569px">Next</div>
</section>

<section class="abs panel sales">
  <div class="panel-head"><span class="head-dot"></span>Sales Statics</div>
  <div class="abs legend"><span class="a"><i></i>Lorem Ipsum</span><span class="b"><i></i>Ipsum Dolar</span></div>
  <svg class="abs chart" width="664" height="214" viewBox="0 0 664 214" font-family="Roboto, Arial, sans-serif" font-size="10" fill="#333">
    <g text-anchor="end">
      <text x="26" y="16">80</text><text x="26" y="37">70</text><text x="26" y="58">60</text>
      <text x="26" y="79">50</text><text x="26" y="100">40</text><text x="26" y="121">30</text>
      <text x="26" y="142">20</text><text x="26" y="162">10</text><text x="26" y="183">0</text>
    </g>
    <path d="M33 118 C60 130,80 150,104 147 C150 140,180 74,237 74 C300 74,370 134,424 134 C480 134,500 114,544 114 C590 114,620 90,648 64 L648 183 L33 183 Z" fill="#f7b4b6" opacity=".85"/>
    <path d="M33 124 C70 128,100 131,130 131 C170 131,200 150,229 150 C265 150,280 98,313 98 C370 98,410 142,453 142 C500 142,530 123,565 123 C600 123,620 134,648 134 L648 183 L33 183 Z" fill="#f06e72" opacity=".95"/>
    <g fill="#fff" stroke="#666" stroke-width="1">
      <circle cx="229" cy="150" r="6"/><circle cx="313" cy="98" r="6"/><circle cx="453" cy="142" r="6"/><circle cx="565" cy="123" r="6"/>
    </g>
    <circle cx="130" cy="131" r="6" fill="#fff" stroke="#f04a50" stroke-width="1.5"/>
    <path d="M122 104 L138 104 L130 114 Z" fill="#f04a50"/>
    <g text-anchor="middle" font-size="9.5">
      <text x="33" y="200">21/Dec</text><text x="88" y="200">22/Dec</text><text x="142" y="200">23/Dec</text>
      <text x="197" y="200">24/Dec</text><text x="251" y="200">25/Dec</text><text x="306" y="200">26/Dec</text>
      <text x="360" y="200">27/Dec</text><text x="415" y="200">28/Dec</text><text x="469" y="200">29/Dec</text>
      <text x="524" y="200">30/Dec</text><text x="578" y="200">31/Dec</text><text x="633" y="200">1/Jan</text>
    </g>
  </svg>
  <div class="abs tip"><b>27</b><span>22/Dec</span><span>7:30 AM</span></div>
</section>

<section class="abs panel customer">
  <div class="panel-head">
    <svg width="13" height="15" viewBox="0 0 13 15"><circle cx="6.5" cy="4" r="3.6" fill="#f04a50"/><path d="M0 15c0-5 2.5-6.5 6.5-6.5S13 10 13 15z" fill="#f04a50"/></svg>
    Select Customer
    <svg class="chev" width="10" height="6" viewBox="0 0 10 6"><path d="M1 1l4 4 4-4" fill="none" stroke="#f04a50" stroke-width="1.6"/></svg>
  </div>
  <div class="abs txn">Transaction: <em>#98565</em></div>
  <span class="abs notes">Add Notes</span>
  <ul class="abs totals">
    <li><span>Subtotal</span><span>$0.00</span></li>
    <li><span>Tax</span><span>$0.00</span></li>
    <li><span>Discount</span><span>$0.00</span></li>
    <li><span>Total</span><span>$0.00</span></li>
    <li><span>Paid</span><span>$0.00</span></li>
  </ul>
  <div class="abs btn btn-save">SAVE &amp; PERK</div>
  <div class="abs btn btn-pay">PAY NOW</div>
</section>

<div class="abs chat">
  <svg width="18" height="16" viewBox="0 0 18 16"><path d="M9 1.5c4 0 7.5 2.6 7.5 6S13 13.5 9 13.5c-1 0-2-.2-2.8-.5L3 14.5l.9-3C2.4 10.3 1.5 9 1.5 7.5c0-3.4 3.5-6 7.5-6z" fill="none" stroke="#fff" stroke-width="1.4"/><circle cx="6" cy="7.5" r=".9" fill="#fff"/><circle cx="9" cy="7.5" r=".9" fill="#fff"/><circle cx="12" cy="7.5" r=".9" fill="#fff"/></svg>
</div>

</body>
</html>
```